Food Safety Consultancy Flyer Design

We need a flyer design for a new company called Tundo Training. New food safety regulations are coming into effect for all food operators in March 2016. My company provides training and resources to support food operators during the transition onto the new Food Control Plan. For the designs we would like to see any of the colours used from the logo which is attached. The flyer will be letting operators know that there are new regulations and we are here to help. Our company offers three packages: 1. Videos (training videos) 2. Webinars and Workshop 3. One-on-one mentoring. Our websites main colour used is the green colour from the logo.
Food service operators: cafes, restaurants etc.
Hospitality

```html
<!DOCTYPE html>
<html lang="en">
<head>
<meta charset="utf-8">
<title>Tundo Training – Food Act 2014 Flyer</title>
<link rel="stylesheet" href="https://fonts.googleapis.com/css2?family=Open+Sans:wght@400;600;700&family=Roboto+Condensed:wght@700&display=swap">
<style>
  :root {
    --green: #1e9448;
    --green-dark: #1b7a3c;
    --blue: #0f5ea8;
    --orange: #f7941d;
    --charcoal: #3a3a3a;
    --slate: #3e5a5c;
    --grey-label: #6b6b6b;
    --text: #3c3c3c;
    --white: #ffffff;
  }
  * { box-sizing: border-box; margin: 0; padding: 0; }
  html, body { width: 900px; height: 1200px; overflow: hidden; background: #f2f2f2; }
  .flyer {
    position: relative; width: 900px; height: 1200px; overflow: hidden;
    font-family: "Open Sans", Arial, sans-serif; color: var(--text);
  }
  .backdrop {
    position: absolute; left: 0; top: 150px; width: 900px; height: 940px;
    background: radial-gradient(ellipse at 45% 55%, #efe3d6 0%, #f7efe7 40%, #fbf8f4 75%);
  }
  .bands { position: absolute; left: 0; top: 0; }
  .brand {
    position: absolute; left: 28px; top: 56px;
    display: flex; align-items: center; gap: 12px;
  }
  .brand-dot { width: 44px; height: 44px; border-radius: 50%; background: var(--orange); flex: none; }
  .brand-name { font-weight: 700; font-size: 27px; color: var(--green); line-height: 1.05; width: 130px; }
  .launch {
    position: absolute; left: 246px; top: 40px; text-align: center;
    font-family: "Roboto Condensed", "Arial Narrow", sans-serif; font-weight: 700;
  }
  .launch-date { color: var(--blue); font-size: 34px; line-height: 1; }
  .launch-year { color: var(--green); font-size: 74px; letter-spacing: 10px; line-height: 1; }
  .divider { position: absolute; left: 462px; top: 44px; width: 4px; height: 92px; background: var(--orange); }
  .headline {
    position: absolute; left: 482px; top: 44px;
    font-family: "Roboto Condensed", "Arial Narrow", sans-serif; font-weight: 700;
    font-size: 34px; line-height: 1.05; color: var(--charcoal);
  }
  .offer {
    position: absolute; left: 417px; top: 150px; width: 466px; height: 372px;
    background: var(--green); border-radius: 0 0 0 22px; color: var(--white);
    text-align: right; padding: 26px 22px 0 0;
  }
  .offer-title { font-size: 40px; font-weight: 600; line-height: 1.1; }
  .offer-tagline { font-size: 25px; font-weight: 600; margin-bottom: 8px; line-height: 1.3; }
  .topics { list-style: none; }
  .topics li {
    font-size: 21px; font-weight: 700; line-height: 35px; color: #0d2a14;
  }
  .topics li::after {
    content: ""; display: inline-block; width: 12px; height: 12px; border-radius: 50%;
    background: var(--orange); margin-left: 14px; vertical-align: middle;
  }
  .intro {
    position: absolute; left: 44px; top: 358px; width: 306px;
    font-size: 19px; line-height: 1.33; color: var(--text);
  }
  .invite {
    position: absolute; left: 0; top: 530px; width: 900px; text-align: center;
    font-size: 24px; font-weight: 700; color: var(--green-dark);
  }
  .packages-label {
    position: absolute; left: 330px; top: 578px; width: 236px; height: 40px;
    background: var(--grey-label); color: var(--white);
    font-size: 24px; font-weight: 600; text-align: center; line-height: 40px;
  }
  .package { position: absolute; color: var(--white); padding: 12px 10px 0 48px; }
  .package-title { font-size: 26px; font-weight: 600; line-height: 1.3; margin-bottom: 8px; }
  .package-text { font-size: 15px; font-weight: 700; line-height: 1.45; }
  .package--videos { left: 183px; top: 628px; width: 584px; height: 112px; background: var(--blue); }
  .package--webinars { left: 105px; top: 752px; width: 590px; height: 134px; background: var(--orange); padding-left: 124px; }
  .package--webinars .package-text { font-size: 14.5px; }
  .package--mentoring { left: 183px; top: 896px; width: 560px; height: 126px; background: var(--green); }
  .chef-badge {
    position: absolute; width: 164px; height: 164px; border-radius: 50%;
    background: radial-gradient(circle at 50% 45%, #e9e9e9 0 28%, var(--slate) 29%);
    border: 7px solid var(--white); box-shadow: 0 2px 6px rgba(0,0,0,.25);
  }
  .chef-badge--videos { left: 19px; top: 616px; }
  .chef-badge--webinars { left: 669px; top: 735px; }
  .chef-badge--mentoring { left: 19px; top: 882px; }
  .chef-standing {
    position: absolute; left: 640px; top: 905px; width: 110px; height: 190px;
    border-radius: 50px 50px 8px 8px;
    background: linear-gradient(#ffffff, #e6e6e6);
    box-shadow: 0 2px 6px rgba(0,0,0,.15);
  }
  .footer {
    position: absolute; left: 0; top: 1092px; width: 900px; height: 108px;
    background: var(--charcoal); color: var(--white);
    display: flex; align-items: center; justify-content: center;
    font-size: 24px; font-weight: 600; letter-spacing: 2px; word-spacing: 6px;
  }
</style>
</head>
<body>
<main class="flyer">
  <div class="backdrop" role="img" aria-label="Soft, faded photograph of a plated meal"></div>

  <svg class="bands" width="900" height="1200" viewBox="0 0 900 1200" aria-hidden="true">
    <path d="M0 0 H900 V150 C640 150 320 200 0 300 Z" fill="#ffffff"/>
    <path d="M0 300 C320 200 640 150 900 150 V178 C640 178 320 228 0 345 Z" fill="#1e9448"/>
    <path d="M0 345 C320 228 640 178 900 178 V198 C640 200 320 250 0 388 Z" fill="#f7941d"/>
    <path d="M900 128 C760 130 640 140 520 158 L900 150 Z" fill="#f7941d"/>
    <path d="M0 1040 C300 1045 600 1040 900 1020 V1092 H0 Z" fill="#3a3a3a"/>
    <path d="M0 1040 C300 1045 600 1040 900 1020 V1035 C600 1056 300 1060 0 1058 Z" fill="#f7941d"/>
    <path d="M0 1022 C300 1030 600 1025 900 1004 V1020 C600 1040 300 1045 0 1040 Z" fill="#1e9448"/>
  </svg>

  <header>
    <div class="brand">
      <span class="brand-dot"></span>
      <span class="brand-name">Tundo Training</span>
    </div>
    <div class="launch">
      <div class="launch-date">ON 1 MARCH</div>
      <div class="launch-year">2016</div>
    </div>
    <span class="divider"></span>
    <h1 class="headline">THE FOOD ACT 2014<br>COMES INTO FORCE</h1>
  </header>

  <section class="offer">
    <h2 class="offer-title">Tundo Training</h2>
    <p class="offer-tagline">Your reputation is our business</p>
    <ul class="topics">
      <li>With up-to-date knowledge on:</li>
      <li>The Food Act 2014</li>
      <li>Food Control Plan requirements</li>
      <li>Verification expectations</li>
      <li>New Food Grading&nbsp; system</li>
      <li>New Fees</li>
    </ul>
  </section>

  <p class="intro">Food service and food retailers will be on Food Control Plans documentation of processes and risk management to produce safe and suitable food.</p>

  <p class="invite">Let us help you transition and understand all there is to know</p>
  <h3 class="packages-label">Our Packages</h3>

  <article class="package package--videos">
    <h4 class="package-title">Videos</h4>
    <p class="package-text">Animated training videos of the FCP6 month subscription-<br>Translated into&nbsp; Mandarin,Japanese, Korean and Hindi</p>
  </article>
  <article class="package package--webinars">
    <h4 class="package-title">Webinars/Workshops</h4>
    <p class="package-text">A range of webinars at times to suit the hospitality<br>industryAND half day training workshops.<br>6 month subscription to the video library is included</p>
  </article>
  <article class="package package--mentoring">
    <h4 class="package-title">One-to-one mentoring</h4>
    <p class="package-text">We come to you and go through<br>the FCP page-by-page</p>
  </article>

  <div class="chef-badge chef-badge--videos" role="img" aria-label="Illustrated chef holding a knife and broccoli"></div>
  <div class="chef-badge chef-badge--webinars" role="img" aria-label="Illustrated chef holding a fork and spatula"></div>
  <div class="chef-badge chef-badge--mentoring" role="img" aria-label="Illustrated chef holding a ladle and pot"></div>
  <div class="chef-standing" role="img" aria-label="Illustrated chef carrying a covered serving dish"></div>

  <footer class="footer">| www.tundotraining.co.nz &nbsp;| info@tundotraining.co.nz |</footer>
</main>
</body>
</html>
```